Voltline Assemblies, Inc. Business Card

Voltline has three operating entities and I'm looking for a standard business card template that can be used for Voltline and the three operating entities that the logo just get swapped out, but has a very similar look and feel. Ultimately if someone had a business card from each, they assume the organizations are related because they all have the same look and feel.
Below are our websites and I will attached the logos for each entity:
https://www.voltlineassemblies.example/
https://www.brantoceramic.example/
https://www.omra-kfsd.example/
https://www.summitbreaker.example/

Target Market(s)

US Voltline

Industry/Entity Type

US Voltline

Contact Information for Business Card

Normal stuff

```html
<!DOCTYPE html>
<html lang="en">
<head>
<meta charset="utf-8">
<title>Voltline Assemblies, Inc. — Business Card Variations</title>
<link href="https://fonts.googleapis.com/css2?family=Montserrat:wght@500;600;700;800&display=swap" rel="stylesheet">
<style>
  :root {
    --page: #ffffff;
    --frame: #111111;
    --navy-deep: #0b1027;
    --navy-mid: #171f45;
    --navy-bright: #202d63;
    --brand-navy: #1f2c63;
    --brand-red: #c5202f;
    --photo-light: #f1f1f1;
    --photo-mid: #d6d6d6;
    --photo-dark: #bdbdbd;
    --ink-light: #ffffff;
  }
  * { box-sizing: border-box; margin: 0; padding: 0; }
  html, body {
    width: 1200px; height: 900px; overflow: hidden;
    background: var(--page);
    font-family: "Montserrat", sans-serif;
  }
  .sheet { position: relative; width: 1200px; height: 900px; }

  .card-frame {
    position: absolute;
    width: 534px; height: 297px;
    border: 1.5px solid var(--frame);
    background: var(--page);
  }
  .card-frame--a { left: 50px;  top: 137px; }
  .card-frame--b { left: 623px; top: 137px; }
  .card-frame--c { left: 50px;  top: 477px; }
  .card-frame--d { left: 623px; top: 477px; }

  .card {
    position: absolute; left: 8.5px; top: 8.5px;
    width: 515px; height: 277px; overflow: hidden;
    background: var(--page);
  }

  .card__photo { position: absolute; left: 0; top: 0; width: 340px; height: 277px; }
  .card__photo--insulator  { background: linear-gradient(135deg, var(--photo-light) 0%, var(--photo-mid) 55%, var(--photo-dark) 100%); }
  .card__photo--substation { background: linear-gradient(180deg, var(--photo-mid) 0%, var(--photo-light) 45%, var(--photo-dark) 100%); }
  .card__photo--yard       { background: linear-gradient(180deg, var(--photo-light) 0%, var(--photo-mid) 60%, var(--photo-dark) 100%); }
  .card__photo--tower      { background: linear-gradient(120deg, var(--photo-mid) 0%, var(--photo-light) 50%, var(--photo-light) 100%); }

  .wordmark {
    position: absolute; left: 10px; width: 310px; top: 160px;
    text-align: center; color: var(--brand-navy); font-weight: 700;
  }
  .wordmark__name { font-size: 38px; line-height: 38px; letter-spacing: -0.5px; text-transform: uppercase; }
  .wordmark__suffix { font-size: 13px; line-height: 18px; letter-spacing: 5px; text-transform: uppercase; margin-top: 2px; }

  .info-panel {
    position: absolute; left: 325px; width: 190px; height: 88px;
    border-radius: 44px 0 0 44px;
    box-shadow: 0 0 0 3.5px var(--page);
    color: var(--ink-light);
  }
  .info-panel--contact { top: 0;   background: var(--navy-deep); }
  .info-panel--web     { top: 94px; background: var(--navy-mid); }
  .info-panel--address { top: 189px; background: var(--navy-bright); }

  .info-panel__icon { position: absolute; left: 25px; top: 32px; width: 26px; height: 26px; }
  .info-panel__text { position: absolute; left: 73px; right: 10px; font-weight: 600; text-transform: uppercase; }

  .contact-name  { font-size: 11px; line-height: 13px; }
  .contact-title { font-size: 6.8px; line-height: 9px; }
  .contact-phone { font-size: 10.5px; line-height: 13px; margin-top: 5px; letter-spacing: 0.3px; }
  .info-panel--contact .info-panel__text { top: 24px; }

  .info-panel--web .info-panel__text { top: 27px; left: 68px; font-size: 9px; line-height: 11px; }
  .web-line + .web-line { margin-top: 10px; }
  .web-line--site { letter-spacing: 0.8px; }

  .info-panel--address .info-panel__text { top: 26px; font-size: 9.5px; line-height: 11.5px; letter-spacing: 0.2px; }
  .info-panel--address .info-panel__icon { left: 28px; top: 25px; width: 20px; height: 36px; }
</style>
</head>
<body>
<main class="sheet">

  <!-- Variation: insulator photo -->
  <section class="card-frame card-frame--a">
    <div class="card">
      <div class="card__photo card__photo--insulator" role="img" aria-label="Faded grayscale photo of a power line insulator and switch hardware"></div>
      <div class="wordmark">
        <div class="wordmark__name">Voltline</div>
        <div class="wordmark__suffix">Assemblies, Inc.</div>
      </div>
      <div class="info-panel info-panel--contact">
        <svg class="info-panel__icon" viewBox="0 0 26 26" aria-hidden="true"><circle cx="13" cy="8" r="5.5" fill="#fff"/><path d="M2 25c0-6 5-9 11-9s11 3 11 9z" fill="#fff"/></svg>
        <div class="info-panel__text">
          <div class="contact-name">Your Name Here</div>
          <div class="contact-title">Your Bespoke Title Here</div>
          <div class="contact-phone">+00 00 000 0000</div>
        </div>
      </div>
      <div class="info-panel info-panel--web">
        <svg class="info-panel__icon" viewBox="0 0 26 26" aria-hidden="true" fill="none" stroke="#fff" stroke-width="1.6"><circle cx="13" cy="13" r="11"/><ellipse cx="13" cy="13" rx="5" ry="11"/><path d="M2 13h22M4 7h18M4 19h18M13 2v22"/></svg>
        <div class="info-panel__text">
          <div class="web-line web-line--site">www.website.com</div>
          <div class="web-line">emails@website.com</div>
        </div>
      </div>
      <div class="info-panel info-panel--address">
        <svg class="info-panel__icon" viewBox="0 0 20 36" aria-hidden="true"><path d="M10 1a9 9 0 0 0-9 9c0 7 9 25 9 25s9-18 9-25a9 9 0 0 0-9-9z" fill="#fff"/><circle cx="10" cy="10" r="3.8" fill="#202d63"/></svg>
        <div class="info-panel__text">
          <div>1 Business Street</div>
          <div>Company Blvd.</div>
          <div>0000</div>
        </div>
      </div>
    </div>
  </section>

  <!-- Variation: substation photo -->
  <section class="card-frame card-frame--b">
    <div class="card">
      <div class="card__photo card__photo--substation" role="img" aria-label="Faded grayscale photo of substation equipment and steel structures"></div>
      <div class="wordmark">
        <div class="wordmark__name">Voltline</div>
        <div class="wordmark__suffix">Assemblies, Inc.</div>
      </div>
      <div class="info-panel info-panel--contact">
        <svg class="info-panel__icon" viewBox="0 0 26 26" aria-hidden="true"><circle cx="13" cy="8" r="5.5" fill="#fff"/><path d="M2 25c0-6 5-9 11-9s11 3 11 9z" fill="#fff"/></svg>
        <div class="info-panel__text">
          <div class="contact-name">Your Name Here</div>
          <div class="contact-title">Your Bespoke Title Here</div>
          <div class="contact-phone">+00 00 000 0000</div>
        </div>
      </div>
      <div class="info-panel info-panel--web">
        <svg class="info-panel__icon" viewBox="0 0 26 26" aria-hidden="true" fill="none" stroke="#fff" stroke-width="1.6"><circle cx="13" cy="13" r="11"/><ellipse cx="13" cy="13" rx="5" ry="11"/><path d="M2 13h22M4 7h18M4 19h18M13 2v22"/></svg>
        <div class="info-panel__text">
          <div class="web-line web-line--site">www.website.com</div>
          <div class="web-line">emails@website.com</div>
        </div>
      </div>
      <div class="info-panel info-panel--address">
        <svg class="info-panel__icon" viewBox="0 0 20 36" aria-hidden="true"><path d="M10 1a9 9 0 0 0-9 9c0 7 9 25 9 25s9-18 9-25a9 9 0 0 0-9-9z" fill="#fff"/><circle cx="10" cy="10" r="3.8" fill="#202d63"/></svg>
        <div class="info-panel__text">
          <div>1 Business Street</div>
          <div>Company Blvd.</div>
          <div>0000</div>
        </div>
      </div>
    </div>
  </section>

  <!-- Variation: switchyard photo -->
  <section class="card-frame card-frame--c">
    <div class="card">
      <div class="card__photo card__photo--yard" role="img" aria-label="Faded grayscale photo of a switchyard with rows of insulators"></div>
      <div class="wordmark">
        <div class="wordmark__name">Voltline</div>
        <div class="wordmark__suffix">Assemblies, Inc.</div>
      </div>
      <div class="info-panel info-panel--contact">
        <svg class="info-panel__icon" viewBox="0 0 26 26" aria-hidden="true"><circle cx="13" cy="8" r="5.5" fill="#fff"/><path d="M2 25c0-6 5-9 11-9s11 3 11 9z" fill="#fff"/></svg>
        <div class="info-panel__text">
          <div class="contact-name">Your Name Here</div>
          <div class="contact-title">Your Bespoke Title Here</div>
          <div class="contact-phone">+00 00 000 0000</div>
        </div>
      </div>
      <div class="info-panel info-panel--web">
        <svg class="info-panel__icon" viewBox="0 0 26 26" aria-hidden="true" fill="none" stroke="#fff" stroke-width="1.6"><circle cx="13" cy="13" r="11"/><ellipse cx="13" cy="13" rx="5" ry="11"/><path d="M2 13h22M4 7h18M4 19h18M13 2v22"/></svg>
        <div class="info-panel__text">
          <div class="web-line web-line--site">www.website.com</div>
          <div class="web-line">emails@website.com</div>
        </div>
      </div>
      <div class="info-panel info-panel--address">
        <svg class="info-panel__icon" viewBox="0 0 20 36" aria-hidden="true"><path d="M10 1a9 9 0 0 0-9 9c0 7 9 25 9 25s9-18 9-25a9 9 0 0 0-9-9z" fill="#fff"/><circle cx="10" cy="10" r="3.8" fill="#202d63"/></svg>
        <div class="info-panel__text">
          <div>1 Business Street</div>
          <div>Company Blvd.</div>
          <div>0000</div>
        </div>
      </div>
    </div>
  </section>

  <!-- Variation: transmission tower photo -->
  <section class="card-frame card-frame--d">
    <div class="card">
      <div class="card__photo card__photo--tower" role="img" aria-label="Faded grayscale photo of a transmission tower with insulator strings"></div>
      <div class="wordmark">
        <div class="wordmark__name">Voltline</div>
        <div class="wordmark__suffix">Assemblies, Inc.</div>
      </div>
      <div class="info-panel info-panel--contact">
        <svg class="info-panel__icon" viewBox="0 0 26 26" aria-hidden="true"><circle cx="13" cy="8" r="5.5" fill="#fff"/><path d="M2 25c0-6 5-9 11-9s11 3 11 9z" fill="#fff"/></svg>
        <div class="info-panel__text">
          <div class="contact-name">Your Name Here</div>
          <div class="contact-title">Your Bespoke Title Here</div>
          <div class="contact-phone">+00 00 000 0000</div>
        </div>
      </div>
      <div class="info-panel info-panel--web">
        <svg class="info-panel__icon" viewBox="0 0 26 26" aria-hidden="true" fill="none" stroke="#fff" stroke-width="1.6"><circle cx="13" cy="13" r="11"/><ellipse cx="13" cy="13" rx="5" ry="11"/><path d="M2 13h22M4 7h18M4 19h18M13 2v22"/></svg>
        <div class="info-panel__text">
          <div class="web-line web-line--site">www.website.com</div>
          <div class="web-line">emails@website.com</div>
        </div>
      </div>
      <div class="info-panel info-panel--address">
        <svg class="info-panel__icon" viewBox="0 0 20 36" aria-hidden="true"><path d="M10 1a9 9 0 0 0-9 9c0 7 9 25 9 25s9-18 9-25a9 9 0 0 0-9-9z" fill="#fff"/><circle cx="10" cy="10" r="3.8" fill="#202d63"/></svg>
        <div class="info-panel__text">
          <div>1 Business Street</div>
          <div>Company Blvd.</div>
          <div>0000</div>
        </div>
      </div>
    </div>
  </section>

</main>
</body>
</html>
```